Simple graphic for a book or slide presentation

We are looking for a style that suits the style of our book. It's title is Harbor. Keeping a calm course through stormy seas. There will be more line drawing/graphics in the book but how you design this image will create the style for all the other simple graphics in the book (once we decide what they are). So this one design will lead to a few more to match the style of this one. We'd like the shape of the overall graphic (i.e the arrows and words/bubbles) to be circular (not a rounded square as appears in the sample attached). Perhaps the words don't need to be in ovals or bound by anything at all; perhaps they do - let's see what you see. We'd like you to choose a font or offer many different fonts you think will capture the practical yet unconventional tone of the book. The book is teaching that managing risks in life is a life-skill that can be learned. The section of the book where this graphic will be placed is called "the power of language" - basically we are saying that thoughts, words and actions create our culture and our destiny. This insight comes from Torvel Pelloru's famous quote:
Carefully watch your thoughts, for they become your words.
Manage and watch your words, for they will become your actions.
Consider and judge your actions, for they have become your habits.
Acknowledge and watch your habits, for they shall become your values.
Understand and embrace your values, for they become your destiny.

Please change the text in the middle of the graphic to say: The Human Culture Cycle

```html
<!DOCTYPE html>
<html lang="en">
<head>
<meta charset="utf-8">
<title>The Human Culture Cycle</title>
<link rel="stylesheet" href="https://fonts.googleapis.com/css2?family=Barlow+Condensed:wght@600&display=swap">
<style>
  :root {
    --paper: #ffffff;
    --ink: #000000;
    --thoughts: #f7c882;
    --words: #98d3f0;
    --actions: #f18bb7;
    --habits: #b490c0;
    --values: #fdeb88;
    --culture: #9fd39b;
  }
  html, body {
    margin: 0;
    padding: 0;
    width: 1200px;
    height: 1200px;
    overflow: hidden;
    background: var(--paper);
  }
  .cycle-diagram {
    display: block;
    width: 1200px;
    height: 1200px;
  }
  .segment--thoughts { fill: var(--thoughts); }
  .segment--words    { fill: var(--words); }
  .segment--actions  { fill: var(--actions); }
  .segment--habits   { fill: var(--habits); }
  .segment--values   { fill: var(--values); }
  .segment--culture  { fill: var(--culture); }
  .stage-label,
  .cycle-title {
    font-family: "Barlow Condensed", "Arial Narrow", sans-serif;
    font-weight: 600;
    fill: var(--ink);
    text-transform: uppercase;
  }
  .stage-label {
    font-size: 108px;
    letter-spacing: 4px;
  }
  .cycle-title {
    font-size: 118px;
    letter-spacing: 1px;
  }
</style>
</head>
<body>
<svg class="cycle-diagram" viewBox="0 0 1920 1920" xmlns="http://www.w3.org/2000/svg" role="img" aria-label="The Human Culture Cycle: thoughts, words, actions, habits, values, culture">
  <defs>
    <path id="outer-track" d="M455,965 A510,510 0 1 1 1475,965 A510,510 0 1 1 455,965"/>
    <path id="inner-track" d="M370,965 A595,595 0 1 0 1560,965 A595,595 0 1 0 370,965"/>
  </defs>

  <g class="ring">
    <path class="segment segment--thoughts" d="M584,320 A750,750 0 0 1 1333,313 L1266,434 L1332,547 L1200,549 L1132,670 A338,338 0 0 0 792,674 L722,554 L787,439 L654,440 Z"/>
    <path class="segment segment--words" d="M1333,313 A750,750 0 0 1 1715,958 L1576,959 L1511,1075 L1444,961 L1304,962 A338,338 0 0 0 1132,670 L1200,549 L1332,547 L1266,434 Z"/>
    <path class="segment segment--actions" d="M1715,958 A750,750 0 0 1 1347,1610 L1277,1492 L1145,1492 L1208,1377 L1139,1258 A338,338 0 0 0 1304,962 L1444,961 L1511,1075 L1576,959 Z"/>
    <path class="segment segment--habits" d="M1347,1610 A750,750 0 0 1 597,1618 L666,1497 L599,1384 L732,1382 L799,1261 A338,338 0 0 0 1139,1258 L1208,1377 L1145,1492 L1277,1492 Z"/>
    <path class="segment segment--values" d="M597,1618 A750,750 0 0 1 216,973 L355,972 L420,857 L487,970 L627,969 A338,338 0 0 0 799,1261 L732,1382 L599,1384 L666,1497 Z"/>
    <path class="segment segment--culture" d="M216,973 A750,750 0 0 1 584,320 L654,440 L787,439 L722,554 L792,674 A338,338 0 0 0 627,969 L487,970 L420,857 L355,972 Z"/>
  </g>

  <g class="stage-labels">
    <text class="stage-label" text-anchor="middle"><textPath href="#outer-track" startOffset="9.8%">Culture</textPath></text>
    <text class="stage-label" text-anchor="middle"><textPath href="#outer-track" startOffset="25%">Thoughts</textPath></text>
    <text class="stage-label" text-anchor="middle"><textPath href="#outer-track" startOffset="42.9%">Words</textPath></text>
    <text class="stage-label" text-anchor="middle"><textPath href="#inner-track" startOffset="7.1%">Values</textPath></text>
    <text class="stage-label" text-anchor="middle"><textPath href="#inner-track" startOffset="25%">Habits</textPath></text>
    <text class="stage-label" text-anchor="middle"><textPath href="#inner-track" startOffset="40.3%">Actions</textPath></text>
  </g>

  <g class="cycle-title-block">
    <text class="cycle-title" x="965" y="846" text-anchor="middle">The</text>
    <text class="cycle-title" x="965" y="953" text-anchor="middle">Human</text>
    <text class="cycle-title" x="965" y="1060" text-anchor="middle">Culture</text>
    <text class="cycle-title" x="965" y="1167" text-anchor="middle">Cycle</text>
  </g>
</svg>
</body>
</html>
```